Bref créative
Velvet Rooms
Home Interiors
Modern
Linnea Parcot Weller
Design Consultant
412 Quillon Lane
Palm beach Gardens, Fl 33587
LinneaParcot@velmorra.example
VelvetRooms.example
My logo is the Velvet Rooms. Would like to incorporate a flur de lis.

```html
<!DOCTYPE html>
<html lang="en">
<head>
<meta charset="utf-8">
<title>Velvet Rooms — Business Card</title>
<link rel="stylesheet" href="https://fonts.googleapis.com/css2?family=Merriweather:wght@400;700&family=Open+Sans:wght@400;600&display=swap">
<style>
  :root {
    --backdrop: #e9e6e2;
    --card: #ffffff;
    --accent-red: #c4161c;
    --band-dark: #1a1a1a;
    --ink: #3a3a3a;
    --ink-soft: #555555;
    --divider: #c9c9c9;
    --art-a: #e2e2e2;
    --art-b: #a8a8a8;
  }
  * { box-sizing: border-box; margin: 0; padding: 0; }
  html, body {
    width: 1200px; height: 780px; overflow: hidden;
    background: var(--backdrop);
  }
  .card {
    position: absolute; left: 75px; top: 90px;
    width: 1050px; height: 600px;
    background: var(--card);
    border-radius: 36px;
    overflow: hidden;
    box-shadow: 0 6px 18px rgba(0,0,0,0.12);
  }
  .edge-band {
    position: absolute; left: 0; top: 0; bottom: 0; width: 34px;
    background: linear-gradient(90deg, #a10f14, var(--accent-red) 60%, #d8262b);
  }
  .edge-rule {
    position: absolute; left: 42px; top: 0; bottom: 0; width: 4px;
    background: var(--band-dark);
  }
  .brand {
    position: absolute; left: 95px; top: 165px;
    width: 400px; height: 250px;
  }
  .brand-art {
    position: absolute; left: 0; top: 0;
    width: 80px; height: 240px;
    border-radius: 30px 30px 14px 14px;
    background: linear-gradient(180deg, var(--accent-red) 0 20%, var(--art-a) 20%, var(--art-b));
    opacity: 0.85;
  }
  .brand-name {
    position: absolute; left: 100px; top: 118px;
    font-family: 'Merriweather', serif; font-weight: 400;
    font-size: 36px; line-height: 1.15; letter-spacing: 1px;
    color: var(--ink);
    white-space: nowrap;
  }
  .brand-name span { display: block; }
  .divider {
    position: absolute; left: 520px; top: 110px;
    width: 2px; height: 390px;
    background: linear-gradient(180deg, transparent, var(--divider) 15%, var(--divider) 85%, transparent);
  }
  .details {
    position: absolute; left: 555px; top: 85px; right: 30px;
    font-family: 'Open Sans', sans-serif;
    color: var(--ink-soft);
  }
  .person-name {
    font-family: 'Merriweather', serif; font-weight: 700;
    font-size: 34px; color: var(--accent-red); line-height: 1.2;
    white-space: nowrap;
  }
  .person-role { font-size: 22px; color: var(--ink); margin-top: 4px; }
  .address { margin-top: 62px; margin-left: 30px; font-size: 22px; line-height: 1.45; }
  .contact-list { list-style: none; margin-top: 22px; margin-left: 30px; }
  .contact-item {
    display: flex; align-items: center; gap: 12px;
    font-size: 22px; line-height: 38px; white-space: nowrap;
  }
  .contact-icon { width: 22px; height: 22px; flex: none; }
</style>
</head>
<body>
  <div class="card">
    <div class="edge-band"></div>
    <div class="edge-rule"></div>

    <div class="brand">
      <div class="brand-art" role="img" aria-label="Illustration of a vase holding a red flower"></div>
      <div class="brand-name"><span>Velvet</span><span>Rooms, LLC</span></div>
    </div>

    <div class="divider"></div>

    <div class="details">
      <div class="person-name">Linnea Parcot Weller</div>
      <div class="person-role">Design Consultant</div>

      <div class="address">
        412 Quillon Lane<br>
        Palm beach Gardens, Fl 33587
      </div>

      <ul class="contact-list">
        <li class="contact-item">
          <svg class="contact-icon" viewBox="0 0 24 24" aria-hidden="true">
            <rect x="6" y="2" width="12" height="20" rx="2" fill="var(--accent-red)"/>
            <rect x="8" y="5" width="8" height="10" fill="#fff"/>
            <circle cx="12" cy="18.5" r="1.3" fill="#fff"/>
          </svg>
          555.014.2271
        </li>
        <li class="contact-item">
          <svg class="contact-icon" viewBox="0 0 24 24" aria-hidden="true">
            <rect x="2" y="9" width="20" height="12" rx="2" fill="var(--accent-red)"/>
            <path d="M5 9 Q5 3 12 3 Q19 3 19 9" stroke="var(--accent-red)" stroke-width="3" fill="none"/>
            <circle cx="12" cy="15" r="3" fill="#fff"/>
          </svg>
          555.019.3842
        </li>
        <li class="contact-item">
          <svg class="contact-icon" viewBox="0 0 24 24" aria-hidden="true">
            <circle cx="12" cy="12" r="11" fill="var(--accent-red)"/>
            <circle cx="12" cy="12" r="3.5" stroke="#fff" stroke-width="2" fill="none"/>
            <path d="M15.5 9 V14 Q15.5 16 17.5 15.5 Q19 15 19 12 A7 7 0 1 0 15 18" stroke="#fff" stroke-width="2" fill="none"/>
          </svg>
          LinneaParcot@velmorra.example
        </li>
        <li class="contact-item">
          <svg class="contact-icon" viewBox="0 0 24 24" aria-hidden="true">
            <circle cx="12" cy="12" r="10" stroke="var(--accent-red)" stroke-width="2" fill="none"/>
            <ellipse cx="12" cy="12" rx="4.5" ry="10" stroke="var(--accent-red)" stroke-width="1.6" fill="none"/>
            <path d="M2 12 H22 M4 7 H20 M4 17 H20" stroke="var(--accent-red)" stroke-width="1.4"/>
          </svg>
          VelvetRooms.example
        </li>
      </ul>
    </div>
  </div>
</body>
</html>
```